Layout for site fence advertising - length approx. 250 cm x 125 cm

The advertising will later be printed on a PVC film and used for events or on sports fields.

Main services :
Your regional contact at
Real estate and business financing
independent insurance advice

```html
<!DOCTYPE html>
<html lang="de">
<head>
<meta charset="utf-8">
<title>Halden Vermögensberatung – Bauzaunbanner</title>
<link rel="stylesheet" href="https://fonts.googleapis.com/css2?family=Nunito:wght@500;600;700&display=swap">
<style>
  :root {
    --brand-blue: #2a5ba8;
    --brand-grey: #5f5f5f;
    --text-grey: #505050;
    --paper: #ffffff;
    --page: #ffffff;
    --frame: #1a1a1a;
    --photo-dark: #5a3f33;
    --photo-light: #d9b8a2;
  }
  html, body {
    margin: 0;
    width: 1200px;
    height: 1200px;
    overflow: hidden;
    background: var(--page);
  }
  .banner {
    position: absolute;
    left: 20px;
    top: 310px;
    width: 1160px;
    height: 578px;
    display: block;
    font-family: "Nunito", sans-serif;
  }
  .banner__frame { fill: var(--paper); stroke: var(--frame); stroke-width: 1.5; }
  .blue { fill: var(--brand-blue); }
  .grey { fill: var(--brand-grey); }
  .divider { stroke: var(--brand-grey); stroke-width: 4; }
  .guide-line { stroke: var(--brand-grey); stroke-width: 1.5; }
  .brand-mark { fill: none; stroke: var(--brand-blue); stroke-width: 5; }
  .brand-name { fill: var(--brand-blue); font-weight: 700; font-size: 26px; }
  .brand-name__suffix { font-size: 21px; }
  .tagline { fill: var(--text-grey); font-weight: 600; font-size: 22px; }
  .service-label { fill: #ffffff; font-weight: 700; font-size: 24px; letter-spacing: -0.3px; }
  .portrait-ring { fill: var(--brand-grey); }
</style>
</head>
<body>
<svg class="banner" viewBox="0 0 1208 602" xmlns="http://www.w3.org/2000/svg">
  <defs>
    <radialGradient id="portraitTone" cx="55%" cy="45%" r="60%">
      <stop offset="0" stop-color="var(--photo-light)"/>
      <stop offset="1" stop-color="var(--photo-dark)"/>
    </radialGradient>
    <clipPath id="portraitClip"><circle cx="940" cy="274" r="232"/></clipPath>
  </defs>

  <rect class="banner__frame" x="0.75" y="0.75" width="1206.5" height="600.5"/>

  <polygon class="blue" points="470,601 715,356 1000,356 1000,226 1207,226 1207,601"/>
  <line class="guide-line" x1="452" y1="601" x2="697" y2="356"/>

  <g class="brand">
    <circle class="brand-mark" cx="135" cy="159" r="82"/>
    <line class="divider" x1="236" y1="70" x2="236" y2="246"/>
    <text class="brand-name" x="252" y="150">Halden Vermögensberatung <tspan class="brand-name__suffix">GmbH</tspan></text>
    <text class="tagline" x="252" y="185">Finanzieren, Versichern, Vorsorgen</text>
  </g>

  <g class="services">
    <path class="blue" d="M48,357 V330 a25,25 0 0 1 25,-25 H255 a25,25 0 0 1 25,25 V357 Z"/>
    <text class="service-label" x="63" y="344">MAIN SERVICES :</text>

    <polygon class="grey" points="48,357 697,357 640,414 48,414"/>
    <text class="service-label" x="63" y="396">YOUR REGIONAL CONTACT AT</text>

    <polygon class="blue" points="48,428 626,428 569,485 48,485"/>
    <text class="service-label" x="63" y="467">REAL ESTATE AND BUSINESS FINANCING</text>

    <polygon class="grey" points="48,499 555,499 498,556 48,556"/>
    <text class="service-label" x="63" y="538">INDEPENDENT INSURANCE ADVICE</text>
  </g>

  <circle class="portrait-ring" cx="940" cy="274" r="255"/>
  <g clip-path="url(#portraitClip)">
    <rect x="708" y="42" width="464" height="464" fill="url(#portraitTone)" role="img" aria-label="Portraitfoto des Beraters"/>
  </g>
</svg>
</body>
</html>
```